Each Lady Ought to Learn Her R.I.M.shape

We need a book cover design for a book that will be used as a confidence coaching tool for women of all races, and walks of life . The title is a play on words because CUP is an acronym that stands for calling, uniqueness, and her purpose. The twist of the book is that this is from a male perspective.
The book will focus on Knowing the Bra types available and how bras represent the different kind of people you need in your life.
Updates

There are certain dynamics requested for this book cover i.e., tape measure, bra etc.  Please view pictures attached to file. i would like to see a book cover with breast covered maybe with hands. 

Target Market(s)

every female in the population of the world from every walk of life from 12-99

Requirements
Must have
• The book cover will also be used for the product line i.e. follow up work book and teaching tools. Measuring tapes, bras and breast are the main theme. Not too explicit that it wont be allowed on the shelves at Pellman and Crowe but I do want it to push the envelope TO THE POINT IT MAKES YOU WANT TO PICK IT UP!
Nice to have
• a woman measuring her breast or bust line .......also bra sizes like 36c 44dd 38b ect.
Should not have
• no naked women or faces of women or below the navel or above the neck pictures if breast revealed they must be covered by hands or bra or flowers ect.

```html
<!DOCTYPE html>
<html lang="en">
<head>
<meta charset="utf-8">
<title>Each Lady Ought to Learn Her R.I.M.shape — Book Cover</title>
<link rel="stylesheet" href="https://fonts.googleapis.com/css2?family=Bungee&display=swap">
<style>
  :root {
    --paper: #f4f4f4;
    --ink: #e2566f;
    --ink-deep: #b8364f;
    --ink-light: #f4a3b1;
  }
  html, body {
    margin: 0;
    padding: 0;
    width: 895px;
    height: 1200px;
    overflow: hidden;
    background: var(--paper);
  }
  .cover {
    box-sizing: border-box;
    width: 895px;
    height: 1200px;
    padding: 80px 40px 90px;
    display: flex;
    flex-direction: column;
    align-items: center;
    justify-content: space-between;
    font-family: "Bungee", "Arial Black", sans-serif;
    color: var(--ink);
    text-transform: uppercase;
    text-align: center;
    white-space: nowrap;
  }
  .title, .subtitle, .author { margin: 0; font-weight: 400; }
  .line {
    display: block;
    line-height: 0.95;
    text-shadow:
      -2px -2px 0 var(--ink-deep),
      2px 2px 0 var(--ink-light);
  }
  .title-top { font-size: 78px; }
  .acronym {
    display: grid;
    grid-template-columns: auto auto;
    grid-template-rows: auto auto;
    align-items: end;
    margin-top: 14px;
  }
  .acronym-her {
    grid-column: 1 / 3;
    justify-self: start;
    font-size: 50px;
    margin-left: 6px;
    margin-bottom: 4px;
  }
  .acronym-letters {
    font-size: 240px;
    line-height: 0.82;
    letter-spacing: -4px;
    text-shadow:
      -4px -4px 0 var(--ink-deep),
      4px 4px 0 var(--ink-light);
  }
  .acronym-shape {
    font-size: 36px;
    margin-left: 8px;
    margin-bottom: 6px;
  }
  .subtitle-sm { font-size: 84px; }
  .subtitle-lg { font-size: 140px; }
  .subtitle-xs { font-size: 64px; margin: 4px 0; }
  .subtitle-md { font-size: 96px; }
  .author { font-size: 64px; }
</style>
</head>
<body>
  <main class="cover">
    <h1 class="title">
      <span class="line title-top">Each Lady Ought</span>
      <span class="line title-top">To Learn</span>
      <span class="acronym">
        <span class="line acronym-her">Her</span>
        <span class="line acronym-letters">R.I.M</span>
        <span class="line acronym-shape">shape</span>
      </span>
    </h1>
    <p class="subtitle">
      <span class="line subtitle-sm">Proportion</span>
      <span class="line subtitle-lg">Counts</span>
      <span class="line subtitle-xs">Through a Man's</span>
      <span class="line subtitle-md">Viewpoint</span>
    </p>
    <p class="line author">By Marcus Hale</p>
  </main>
</body>
</html>
```